Home Health Care Agency Needs a Website (Seeking a PSD)

We need a user friendly website for a Home Health Care Agency. Our service is for the elderly and disabled. Frequently the busy professional middle-aged married daughter will use the website to arrange in-home care for an aging parent. Therefore, our website is primarily geared towards middle-aged women. In-home care is typically 24 hours a day so, a feeling of trustworthiness and security should be effectively conveyed. (Seeking a PSD- however, if you also offer coding, please let us know the cost.)

Target Market(s)

Frequently the busy professional middle-aged married daughter (possibly out of state) will use the website to arrange in-home care for an aging parent.

Industry/Entity Type

Security

Requirements
Must have
• Website must be clean, uncluttered and professional. The following menu pages are requested: Home, About Us, Services, Resources, FAQ, Employment & Contact.
Should not have
• Must not be too whimsical.

```html
<!DOCTYPE html>
<html lang="en">
<head>
<meta charset="utf-8">
<title>Harbor Home Health</title>
<link rel="stylesheet" href="https://fonts.googleapis.com/css2?family=Open+Sans:wght@400;600;700&family=Oswald:wght@300;400&display=swap">
<style>
:root{
  --sky:#4cc7ef;
  --sky-deep:#1aa8e6;
  --ink:#222;
  --muted:#555;
  --navy:#34465f;
  --page:#eceeef;
  --dark:#444343;
  --white:#fff;
}
*{margin:0;padding:0;box-sizing:border-box}
html,body{width:1200px;height:1125px;overflow:hidden}
body{background:var(--page);font-family:"Open Sans",sans-serif;color:var(--ink);position:relative}
.site{position:absolute;left:110px;top:0;width:982px;height:1125px;background:linear-gradient(#fff 0,#fff 850px,#efefef 1050px)}
.abs{position:absolute}
.header{left:123px;top:0;width:954px;height:130px;background:var(--white);z-index:2}
.brand{left:20px;top:22px;display:flex;align-items:center;gap:8px}
.brand-dot{width:18px;height:18px;border-radius:50%;background:var(--sky)}
.brand-name{font-weight:700;font-size:26px;line-height:27px;color:var(--sky);width:110px}
.social{right:8px;top:14px;display:flex;gap:24px}
.social span{width:18px;height:18px;border-radius:50%;background:#c4c4c4}
.nav{left:0;top:84px;width:954px;font-size:16px;color:#555}
.nav a{position:absolute;color:inherit;text-decoration:none;white-space:nowrap}
.nav a.current{color:var(--sky-deep);font-weight:600;border-bottom:3px solid var(--sky);padding:0 4px 2px}
.hero-photo{left:110px;top:100px;width:656px;height:408px;background:linear-gradient(160deg,#5b8a3a,#8cb55a 55%,#a79a8a)}
.hero-panel{left:766px;top:100px;width:326px;height:408px;background:var(--sky);color:var(--white);text-align:center}
.hero-panel h1{font-weight:400;font-size:29px;line-height:37px;margin-top:97px}
.hero-panel p{font-size:14px;line-height:21px;margin:18px 24px 0}
.arrow{top:290px;color:var(--white);font-size:40px;font-weight:300;z-index:1}
.sidebar{left:112px;top:523px;width:242px;height:510px;background:var(--white);box-shadow:2px 2px 4px rgba(0,0,0,.25)}
.sidebar h3{position:absolute;left:13px;font-size:16px;line-height:22px;font-weight:700;color:var(--sky);white-space:nowrap}
.sidebar ul{position:absolute;left:12px;top:40px;list-style:none;font-size:13px;line-height:21px}
.sidebar li{white-space:nowrap}
.sidebar li::before{content:"";display:inline-block;width:7px;height:7px;background:#333;margin-right:11px;vertical-align:1px}
.video{left:10px;top:333px;width:229px;height:151px;background:linear-gradient(135deg,#c9a096,#e6c3c6)}
.play{left:94px;top:56px;width:40px;height:40px;border-radius:50%;background:rgba(220,220,220,.85);display:flex;align-items:center;justify-content:center}
.section-title{left:380px;top:524px;font-size:22px;font-weight:400;color:var(--navy)}
.service{width:240px;text-align:center}
.service .circle{width:200px;height:200px;border-radius:50%;margin:0 auto;background:radial-gradient(circle at 40% 40%,#d8d8d8,#6f6f6f);box-shadow:2px 2px 3px rgba(0,0,0,.3)}
.service h2{font-size:17px;font-weight:700;margin-top:16px;line-height:22px}
.service p{font-size:12.5px;line-height:21px;color:#333;margin:4px 8px 0}
.more{display:inline-block;width:75px;height:40px;margin-top:18px;background:linear-gradient(#3fd0ff,#08a4e8);color:var(--white);font-family:"Oswald",sans-serif;font-weight:300;font-size:16px;line-height:40px;box-shadow:0 2px 3px rgba(0,0,0,.25)}
.footer{left:110px;top:1058px;width:982px;height:67px;background:var(--dark);color:#ddd;font-size:13px}
.footer a{position:absolute;top:13px;color:#fff;text-decoration:underline;white-space:nowrap}
.copyright{position:absolute;top:38px;width:100%;text-align:center;color:#bbb}
</style>
</head>
<body>
<div class="site"></div>

<header class="abs header">
  <div class="abs brand"><span class="brand-dot"></span><span class="brand-name">Harbor Home Health</span></div>
  <div class="abs social" aria-label="Social links"><span></span><span></span><span></span><span></span><span></span></div>
  <nav class="abs nav">
    <a class="current" style="left:272px">Home</a>
    <a style="left:362px">About Us</a>
    <a style="left:468px">Services</a>
    <a style="left:561px">Resources</a>
    <a style="left:663px">FAQ</a>
    <a style="left:734px">Employment</a>
    <a style="left:864px">Contact Us</a>
  </nav>
</header>

<div class="abs hero-photo" role="img" aria-label="Caregiver walking with an elderly man in a wheelchair through a green park"></div>
<span class="abs arrow" style="left:120px">&lt;</span>
<span class="abs arrow" style="left:722px">&gt;</span>
<section class="abs hero-panel">
  <h1>Maecenas cursus,<br>vitae tincidmt egestas</h1>
  <p>Lorem ipsum dolor sit amet, consectetur adipiscing elit. Maecenas cursus, felis vitae tincidunt egestas, velit lorem tristique mi</p>
</section>

<aside class="abs sidebar">
  <h3 style="top:4px">Lorem ipsum&nbsp; elit</h3>
  <ul>
    <li>Lorem ipsum dolor sit amet</li>
    <li>Consectetur adipiscing elit</li>
    <li>Maecenas cursus</li>
    <li>Felis vitae tincidunt egestas</li>
    <li>Velit lorem tristique mi</li>
    <li>Lorem ipsum dolor sit amet</li>
    <li>Consectetur adipiscing elit</li>
    <li>Maecenas cursus</li>
    <li>Felis vitae tincidunt egestas</li>
    <li>Velit lorem tristique mi</li>
  </ul>
  <h3 style="top:307px">Lorem ipsum&nbsp; elit</h3>
  <div class="abs video" role="img" aria-label="Video still of joined hands resting on a pink knitted blanket">
    <div class="abs play"><svg width="16" height="18" viewBox="0 0 16 18"><path d="M2 1 L15 9 L2 17 Z" fill="#777"/></svg></div>
  </div>
</aside>

<h2 class="abs section-title">WHAT WE DO</h2>

<article class="abs service" style="left:359px;top:577px">
  <div class="circle" role="img" aria-label="Caregiver helping an elderly woman"></div>
  <h2>Consectetur adipiscing</h2>
  <p>Lorem ipsum dolor sit amet, consectetur adipiscing elit. Maecenas cursus, felis vitae tincidunt egestas, velit lorem tristique mi</p>
  <span class="more">MORE</span>
</article>
<article class="abs service" style="left:613px;top:579px">
  <div class="circle" role="img" aria-label="Nurse comforting an elderly patient"></div>
  <h2>Maecenas cursus</h2>
  <p>Lorem ipsum dolor sit amet, consectetur adipiscing elit. Maecenas cursus, felis vitae tincidunt egestas, velit lorem tristique mi</p>
  <span class="more">MORE</span>
</article>
<article class="abs service" style="left:854px;top:577px">
  <div class="circle" role="img" aria-label="Nurse pushing a smiling elderly woman in a wheelchair"></div>
  <h2>Corem isumit</h2>
  <p>Lorem ipsum dolor sit amet, consectetur maecenas cursus, felis vitae tincidunt egestas, velit lorem</p>
  <span class="more">MORE</span>
</article>

<footer class="abs footer">
  <a style="left:302px">Lorem ipsum</a>
  <a style="left:404px">Sit decor</a>
  <a style="left:475px">Gravida</a>
  <a style="left:551px">Metus</a>
  <a style="left:626px">Tincidunt</a>
  <div class="copyright">copyright information</div>
</footer>
</body>
</html>
```